dog food*

We need design for 10 kg pack of dog food (big dogs 12 month),must be 4-5 colors.

I’m producer of dog food
Target market is for normal people(food is cheap)
No ideas fo design and colors
No have site and facebook

```html
<!DOCTYPE html>
<html lang="en">
<head>
<meta charset="utf-8">
<title>Adult Complete Nutrition – 10 kg pack</title>
<link href="https://fonts.googleapis.com/css2?family=Montserrat:ital,wght@0,400;0,600;0,800;1,600&family=Oswald:wght@400;500&display=swap" rel="stylesheet">
<style>
  :root{
    --amber:#E09A2E;
    --slate:#6B6C6E;
    --sky:#A3C3D6;
    --wine:#9B1F2C;
    --white:#FFFFFF;
    --bone:#5E6064;
    --flame:#D8602A;
    --leaf:#9CC23A;
    --ink:#3A3A3A;
  }
  *{box-sizing:border-box;margin:0;padding:0}
  html,body{width:730px;height:1200px;overflow:hidden;background:#FFFFFF}
  body{position:relative;font-family:'Montserrat',sans-serif}

  .pack{position:absolute;left:160px;width:410px;height:576px;overflow:hidden;background:var(--sky)}
  .pack--amber{top:16px;--face:var(--amber)}
  .pack--slate{top:608px;--face:var(--slate)}
  .pack__wave{position:absolute;inset:0;width:100%;height:100%}

  .brand-block{position:absolute;left:150px;top:0;width:106px;height:100px;background:var(--wine);
    display:flex;align-items:flex-end;justify-content:center;padding-bottom:10px}
  .brand-block__name{color:var(--white);font-weight:400;font-size:15px;letter-spacing:.5px}

  .title{position:absolute;left:150px;top:110px;width:110px;color:var(--white);text-align:left}
  .title__main{display:block;font-weight:800;font-size:30px;line-height:32px;letter-spacing:.5px;
    border-bottom:1px solid var(--white);padding-bottom:1px;width:105px}
  .title__sub{display:block;font-weight:800;font-size:17px;line-height:18px;letter-spacing:.3px}
  .age{position:absolute;left:163px;top:182px;display:flex;align-items:center;gap:4px;
    color:var(--white);font-size:7.5px;font-weight:400}
  .age__tag{background:var(--wine);border:1px solid var(--white);border-radius:6px;padding:1px 4px;font-weight:800;font-size:7px}

  .photo{position:absolute;left:102px;top:204px;width:193px;height:267px;border-radius:40% 45% 0 0 / 30% 30% 0 0}
  .pack--amber .photo{background:linear-gradient(160deg,#7A4A22 0%,#B8753A 30%,#EFE9E0 60%,#FFFFFF 100%)}
  .pack--slate .photo{background:linear-gradient(170deg,#3E3E40 0%,#9A9A9C 40%,#E4E4E4 75%,#F4F4F4 100%)}

  .side{position:absolute;top:91px;width:278px;height:38px;transform-origin:0 0;transform:rotate(-90deg) translateX(-278px);
    color:var(--white);line-height:18px}
  .side--left{left:33px}
  .side--right{left:337px}
  .side__claim{display:block;font-weight:800;font-size:15.5px;letter-spacing:.2px;white-space:nowrap}
  .side__sub{display:block;font-weight:600;font-size:12.5px;white-space:nowrap}
  .pack--slate .side--left .side__sub{color:#A9AAAC}

  .origin{position:absolute;top:412px;font-family:'Oswald',sans-serif;font-size:5px;color:var(--ink)}
  .origin--left{left:40px}
  .origin--right{left:346px}
  .weight-tag{position:absolute;top:421px;width:61px;height:14px;background:var(--wine);border:1px solid var(--white);
    border-radius:3px;color:var(--white);font-size:7.5px;display:flex;align-items:center;justify-content:center}
  .weight-tag--left{left:21px}
  .weight-tag--right{left:327px}

  .nutrients{position:absolute;left:160px;top:355px;display:flex;gap:7px}
  .nutrient{width:18px;display:flex;flex-direction:column;align-items:center}
  .nutrient__dial{width:17px;height:17px;border-radius:50%;background:var(--white);border:1.5px solid var(--wine);
    font-family:'Oswald',sans-serif;font-size:7px;color:var(--ink);display:flex;align-items:center;justify-content:center}
  .nutrient__dial--fat{border-color:var(--leaf)}
  .nutrient__label{margin-top:2px;font-family:'Oswald',sans-serif;font-size:4.5px;color:var(--ink)}

  .claims{position:absolute;left:108px;top:386px;display:flex;gap:5px}
  .claim{width:42px;display:flex;flex-direction:column;align-items:center}
  .claim__bone{width:42px;height:15px;border-radius:8px;background:var(--bone);color:var(--white);
    font-weight:800;font-size:9px;display:flex;align-items:center;justify-content:center}
  .claim__bone--full{background:var(--flame)}
  .claim__text{margin-top:2px;font-family:'Oswald',sans-serif;font-size:4.2px;line-height:5px;text-align:center;color:var(--ink)}

  .weight-main{position:absolute;left:161px;top:428px;width:83px;height:27px;background:var(--wine);border-radius:0 0 4px 4px;
    color:var(--white);font-size:10px;display:flex;align-items:center;justify-content:center}
</style>
</head>
<body>

<section class="pack pack--amber" aria-label="Adult dog food pack, amber variant">
  <svg class="pack__wave" viewBox="0 0 583 820" preserveAspectRatio="none" aria-hidden="true">
    <rect width="583" height="820" fill="var(--face)"/>
    <path d="M583,10 C480,80 420,180 415,300 C410,420 350,470 250,510 C150,550 60,560 0,615 L0,820 L583,820 Z" fill="var(--sky)"/>
  </svg>
  <div class="brand-block"><span class="brand-block__name">HOUNDRY</span></div>
  <h1 class="title"><span class="title__main">ADULT</span><span class="title__sub">COMPLETE</span><span class="title__sub">NUTRITION</span></h1>
  <p class="age"><span class="age__tag">ADULT</span>1+ YEARS</p>
  <div class="photo" role="img" aria-label="Photo of a brown and white terrier looking upward"></div>
  <p class="side side--left"><span class="side__claim">NATURAL FOOD FOR ADULT DOGS</span><span class="side__sub">with added vitamins &amp; chelated minerals</span></p>
  <p class="side side--right"><span class="side__claim">NATURAL FOOD FOR ADULT DOGS</span><span class="side__sub">with added vitamins &amp; chelated minerals</span></p>
  <div class="nutrients">
    <div class="nutrient"><span class="nutrient__dial">28%</span><span class="nutrient__label">PROTEIN</span></div>
    <div class="nutrient"><span class="nutrient__dial nutrient__dial--fat">16%</span><span class="nutrient__label">FAT</span></div>
    <div class="nutrient"><span class="nutrient__dial">4%</span><span class="nutrient__label">FIBER</span></div>
  </div>
  <div class="claims">
    <div class="claim"><span class="claim__bone claim__bone--full">100%</span><span class="claim__text">100% COMPLETE<br>&amp; BALANCED FOOD<br>FOR ADULT DOGS</span></div>
    <div class="claim"><span class="claim__bone">NO</span><span class="claim__text">HIGH FRUCTOSE<br>CORN SYRUP</span></div>
    <div class="claim"><span class="claim__bone">NO</span><span class="claim__text">ARTIFICIAL<br>FLAVORS</span></div>
    <div class="claim"><span class="claim__bone">NO</span><span class="claim__text">ADDED<br>SUGAR</span></div>
  </div>
  <span class="origin origin--left">MADE IN EU</span>
  <span class="origin origin--right">MADE IN EU</span>
  <span class="weight-tag weight-tag--left">NET WT 10kg</span>
  <span class="weight-tag weight-tag--right">NET WT 10kg</span>
  <span class="weight-main">NET WT 10kg</span>
</section>

<section class="pack pack--slate" aria-label="Adult dog food pack, slate variant">
  <svg class="pack__wave" viewBox="0 0 583 820" preserveAspectRatio="none" aria-hidden="true">
    <rect width="583" height="820" fill="var(--face)"/>
    <path d="M583,10 C480,80 420,180 415,300 C410,420 350,470 250,510 C150,550 60,560 0,615 L0,820 L583,820 Z" fill="var(--sky)"/>
  </svg>
  <div class="brand-block"><span class="brand-block__name">HOUNDRY</span></div>
  <h1 class="title"><span class="title__main">ADULT</span><span class="title__sub">COMPLETE</span><span class="title__sub">NUTRITION</span></h1>
  <p class="age"><span class="age__tag">ADULT</span>1+ YEARS</p>
  <div class="photo" role="img" aria-label="Black and white photo of a merle shepherd dog facing forward"></div>
  <p class="side side--left"><span class="side__claim">NATURAL FOOD FOR ADULT DOGS</span><span class="side__sub">with added vitamins &amp; chelated minerals</span></p>
  <p class="side side--right"><span class="side__claim">NATURAL FOOD FOR ADULT DOGS</span><span class="side__sub">with added vitamins &amp; chelated minerals</span></p>
  <div class="nutrients">
    <div class="nutrient"><span class="nutrient__dial">28%</span><span class="nutrient__label">PROTEIN</span></div>
    <div class="nutrient"><span class="nutrient__dial nutrient__dial--fat">16%</span><span class="nutrient__label">FAT</span></div>
    <div class="nutrient"><span class="nutrient__dial">4%</span><span class="nutrient__label">FIBER</span></div>
  </div>
  <div class="claims">
    <div class="claim"><span class="claim__bone claim__bone--full">100%</span><span class="claim__text">100% COMPLETE<br>&amp; BALANCED FOOD<br>FOR ADULT DOGS</span></div>
    <div class="claim"><span class="claim__bone">NO</span><span class="claim__text">HIGH FRUCTOSE<br>CORN SYRUP</span></div>
    <div class="claim"><span class="claim__bone">NO</span><span class="claim__text">ARTIFICIAL<br>FLAVORS</span></div>
    <div class="claim"><span class="claim__bone">NO</span><span class="claim__text">ADDED<br>SUGAR</span></div>
  </div>
  <span class="origin origin--left">MADE IN EU</span>
  <span class="origin origin--right">MADE IN EU</span>
  <span class="weight-tag weight-tag--left">NET WT 10kg</span>
  <span class="weight-tag weight-tag--right">NET WT 10kg</span>
  <span class="weight-main">NET WT 10kg</span>
</section>

</body>
</html>
```